Velmora van graphics, back doors wrapped sides and bonnet open to suggestions

I would like to have my van designed for some graphics. It would be nice to stand out from the crowd but not an over powering design, we have tried a few different designs ourselves but sometimes its better for inspiration from elsewhere. My old van image attached, new van is silver as per PDF. Our colours are dark blue and light blue but not sure how these would look on silver van. Possibly orange with anthracite grey would be nice

Target Market(s)

Professional slick look for passing trade to turn heads

Industry/Entity Type

Signage and graphics

Font styles to use
Sans Serif

Colors

Designer to choose colors to be used in the design.

Requirements
Must have
• Branding / logo
Nice to have
• Back doors fully wrapped

```html
<!DOCTYPE html>
<html lang="en">
<head>
<meta charset="utf-8">
<title>Velmora Signs &amp; Graphics – Van Wrap Side Panel</title>
<link href="https://fonts.googleapis.com/css2?family=Montserrat:wght@600;700&display=swap" rel="stylesheet">
<style>
  :root {
    --backdrop: #ededed;
    --wrap-dark: #0d0812;
    --wrap-plum: #2a1338;
    --streak-violet: #7a3c9e;
    --streak-magenta: #9b2a6e;
    --type-silver: #cdcdd1;
  }
  html, body {
    margin: 0;
    padding: 0;
    width: 1200px;
    height: 537px;
    overflow: hidden;
    background: var(--backdrop);
  }
  .wrap-artwork {
    display: block;
    width: 1200px;
    height: 537px;
  }
  .brand-name {
    font-family: "Montserrat", sans-serif;
    font-weight: 700;
    font-size: 42px;
    fill: var(--type-silver);
    letter-spacing: 1px;
  }
  .brand-mark { fill: var(--type-silver); }
  .contact-phone,
  .contact-web {
    font-family: "Montserrat", sans-serif;
    font-weight: 700;
    fill: var(--type-silver);
  }
  .contact-phone { font-size: 28px; }
  .contact-web { font-size: 26px; }
</style>
</head>
<body>
<svg class="wrap-artwork" viewBox="0 0 1200 537" xmlns="http://www.w3.org/2000/svg" role="img" aria-label="Flat side-panel van wrap artwork for Velmora Signs and Graphics">
  <defs>
    <linearGradient id="wrap-base" x1="0" y1="1" x2="1" y2="0">
      <stop offset="0" stop-color="var(--wrap-plum)"/>
      <stop offset="0.45" stop-color="var(--wrap-dark)"/>
      <stop offset="1" stop-color="var(--wrap-dark)"/>
    </linearGradient>
    <linearGradient id="streak-glow" x1="0" y1="0" x2="1" y2="0">
      <stop offset="0" stop-color="var(--streak-magenta)" stop-opacity="0.9"/>
      <stop offset="0.5" stop-color="var(--streak-violet)" stop-opacity="0.75"/>
      <stop offset="1" stop-color="var(--streak-violet)" stop-opacity="0"/>
    </linearGradient>
    <clipPath id="wrap-clip">
      <path d="M85 262 C150 230 250 160 330 145 L560 128 C760 100 940 62 1085 45 L1095 250 C900 272 760 310 650 350 C520 392 380 400 280 396 C180 390 110 360 85 320 Z"/>
    </clipPath>
  </defs>

  <g class="wrap-panel" clip-path="url(#wrap-clip)">
    <rect class="wrap-panel__base" x="0" y="0" width="1200" height="537" fill="url(#wrap-base)"/>
    <g class="wrap-panel__streaks" transform="rotate(-14 600 260)">
      <rect x="60" y="250" width="1100" height="46" fill="url(#streak-glow)" opacity="0.55"/>
      <rect x="60" y="282" width="1000" height="8" fill="url(#streak-glow)"/>
      <rect x="120" y="230" width="950" height="4" fill="url(#streak-glow)" opacity="0.7"/>
      <rect x="60" y="310" width="800" height="3" fill="url(#streak-glow)" opacity="0.6"/>
      <rect x="200" y="210" width="900" height="18" fill="url(#streak-glow)" opacity="0.3"/>
    </g>
  </g>

  <g class="wrap-type">
    <g class="brand-lockup" transform="rotate(-11 340 262)">
      <circle class="brand-mark" cx="318" cy="248" r="11"/>
      <text class="brand-name" x="340" y="262">VELMORA SIGNS &amp; GRAPHICS</text>
    </g>
    <text class="contact-web" x="560" y="322" transform="rotate(-11 560 322)">velmorasigns.co.uk</text>
    <text class="contact-phone" x="150" y="360" transform="rotate(-11 150 360)">0131 555 0194</text>
  </g>
</svg>
</body>
</html>
```